依頼詳細
犬と一緒にアウトドアを楽しめる商品の企画・製造・販売を手掛けます。
先日当サイトで募集したロゴが確定しましたので、そちらを用いた名刺のデザイン案をお寄せください。名刺は2、3色以内で活版印刷を予定しています(単色も可)ので、グラデーションなどを使用しないデザインをお願いいたします。
記載項目
以下の項目が含まれていれば、レイアウトなども含め特に制限はありません。
表面は「屋号」「役職」「氏名」「氏名ローマ字」「郵便番号」「所在地1」「所在地2」「電話番号」「メールアドレス」「URL」
裏面は「ロゴ」キャラだけ文字だけでも可
希望イメージ
シンプル 複雑
単色 カラフル
暗い 明るい
日常 高級
遊び心 厳粛
未来的 伝統的
女性的 男性的
希望する色
納品ファイル
• 高解像度JPG (.jpg)
• イラストレーター形式 (.ai)
• PNG形式 (.png)
補足説明
ブランド名
PIREL(ぴれる)※屋号ではない
所在地について
「所在地1:都道府県市区町村番地」「所在地2:建物名フロア」となります。
例)
〒1234567
所在地1県所在地1市所在地1区所在地1-2-3
所在地2ビル所在地2階

活版印刷での名刺を想定しておりましたので割とシンプルなデザインの提案が多い中、
ブランド特性に配慮いただき遊び心を取り入れていただいたところがポイントと
なりました。

事業が動き出したばかりということもあり、今後もご協力をいただく機会があるかと
思いますので、その節はまた提案いただけると助かります。

```html
<!DOCTYPE html>
<html lang="ja">
<head>
<meta charset="utf-8">
<title>PIREL 名刺 表面</title>
<link rel="stylesheet" href="https://fonts.googleapis.com/css2?family=Noto+Sans+JP:wght@300;400&family=Noto+Serif+JP:wght@300&display=swap">
<style>
  :root {
    --paper: #ffffff;
    --ink: #3a3a3a;
    --ink-soft: #8f8f8f;
  }
  html, body {
    margin: 0;
    padding: 0;
    width: 726px;
    height: 1200px;
    overflow: hidden;
    background: var(--paper);
  }
  .card {
    position: relative;
    width: 726px;
    height: 1200px;
    background: var(--paper);
    color: var(--ink);
    font-family: "Noto Sans JP", sans-serif;
  }
  .trade-name {
    position: absolute;
    left: 10px;
    top: 118px;
    margin: 0;
    font-size: 31px;
    font-weight: 400;
    color: var(--ink-soft);
    letter-spacing: 2px;
    transform: rotate(-58deg);
    transform-origin: left center;
    white-space: nowrap;
    top: 250px;
    left: 70px;
  }
  .title {
    position: absolute;
    left: 145px;
    top: 392px;
    margin: 0;
    font-size: 31px;
    font-weight: 400;
  }
  .name {
    position: absolute;
    left: 145px;
    top: 440px;
    margin: 0;
    font-family: "Noto Serif JP", serif;
    font-weight: 300;
    font-size: 74px;
    line-height: 1.2;
    letter-spacing: 4px;
    white-space: nowrap;
  }
  .name .given { margin-left: 62px; }
  .romaji {
    position: absolute;
    top: 548px;
    margin: 0;
    font-size: 24px;
    font-weight: 400;
    letter-spacing: 4px;
  }
  .romaji.family { left: 162px; }
  .romaji.given { left: 430px; }
  .contact {
    position: absolute;
    left: 145px;
    top: 658px;
    margin: 0;
    font-size: 31px;
    line-height: 44px;
    font-weight: 400;
    font-style: normal;
    white-space: nowrap;
  }
  .contact .address-2 { margin-bottom: 2px; }
  .contact .mail { margin-top: 4px; }
  .url {
    position: absolute;
    left: 470px;
    top: 1160px;
    margin: 0;
    font-size: 30px;
    font-weight: 400;
    color: var(--ink-soft);
    letter-spacing: 1px;
    transform: rotate(-55deg);
    transform-origin: left center;
    white-space: nowrap;
  }
</style>
</head>
<body>
  <main class="card">
    <p class="trade-name">屋号が入ります</p>

    <p class="title">代表取締役</p>
    <h1 class="name"><span class="family">山田</span><span class="given">太郎</span></h1>
    <p class="romaji family">Yamada</p>
    <p class="romaji given">Taro</p>

    <address class="contact">
      <div class="postal">〒123-4567</div>
      <div class="address-1">都道府県市区町村●●●●</div>
      <div class="address-2">●●●●ビル0F</div>
      <div class="tel">tel:080-1234-5678</div>
      <div class="mail">mail:info@pirel.com</div>
    </address>

    <p class="url">https://pirel.com</p>
  </main>
</body>
</html>
```